PowerPoint Design Project

Design Brief
Corvanta is updating its stationary templates to reflect the company’s position as market leader in smart-location based solutions.
Using the existing Corvanta logo and corporate colours, create an engaging and visually appealing PowerPoint presentation template identity that works when printed on A4 and US Letter sized paper.
The successful designs will complement the current look and feel of the Corvanta website (www.corvanta-example.net) and communicate that Corvanta is a dynamic and modern technology company that is at the cutting edge of innovation.
Corvanta Brand
Corvanta stands for Precision Location Technology. The brand represents both a unique, highly innovative platform product and a mature consulting and support organisation dedicated to delivering solutions to blue-chip customer problems. The orange colour implies creativity while blue evokes trust and a rational approach. “Ubi” is Latin and means “where”, so the brand directly addresses the focus of the company: location. “Sense” can mean that we have sensing technology to support our precision location aware applications and solutions, but also that we make sensible use of location data to improve customer processes.
Corvanta Corporate Profile
Corvanta is a market leader of location-based Smart Factory Solutions which enables companies to optimise their business processes. By keeping track of key assets, Corvanta solutions bring clarity to complex operations in industries while also improving quality and reliability. Corvanta uses a unique combination of advancefd industry knowledge and an experienced team to deliver effective and superior solutions that offer unprecedented visibility, control and accuracy, delivering time and cost savings. Corvanta solutions are easy to implement and flexible to a particular business’s needs, no matter which area of the globe they operate in.
Corvanta offers two location-oriented products; RTLS (Real-time Location Solutions) and Geospatial Systems and operates in a number of industries ranging from manufacturing and utilities to telecommunications and is used by a number of blue chip customers across the world, such as KLT, Skyvane, Groundmole, Fenwick Power, RAL and Nordische Fernmelde.
Corvanta Corporate Colours
Orange:
Pantone 021C
R: 237 / G: 110 / B: 0
C: 0 / M: 53 / Y: 100 / K: 0
Hex #ED6E00
Dark Blue:
Pantone 662C
R: 15 / G: 31 / B: 122
C: 100 / M: 71 / Y: 0 / K:0
Hex #0F1F7A
Light Blue:
Pantone 300C
R: 0 / G: 110 / B: 199
C: 100 / M: 44 / Y: 0 / K:0
Hex #006EC7
Corvanta Corporate Fonts
The preferred font is Tahoma for Title, Topics and Print. In certain situations, Arial is an acceptable alternative.
Target Market(s)
Manufacturing industry, Automotive and Aerospace
Industry/Entity Type
Telecommunications
Look and feel

```html
<!DOCTYPE html>
<html lang="en">
<head>
<meta charset="utf-8">
<title>Corvanta Presentation Template</title>
<link rel="stylesheet" href="https://fonts.googleapis.com/css2?family=Noto+Sans:wght@400;700&family=Carlito:wght@400;700&display=swap">
<style>
  :root {
    --orange: #ed6e00;
    --orange-deep: #c0480a;
    --dark-blue: #0f1f7a;
    --light-blue: #006ec7;
    --band-start: #0a6cc6;
    --band-end: #1b1d27;
    --strip-blue: #1a8fe0;
    --ink: #111111;
    --grey: #8a8a8a;
    --page: #ffffff;
    --slide: #ffffff;
  }
  * { box-sizing: border-box; margin: 0; padding: 0; }
  html, body { width: 1200px; height: 1000px; overflow: hidden; background: var(--page); }
  body { position: relative; font-family: "Noto Sans", Tahoma, sans-serif; color: var(--ink); }

  .slide {
    position: absolute;
    background: var(--slide);
    box-shadow: 3px 4px 5px rgba(0,0,0,0.35);
    overflow: hidden;
  }
  .slide--title { left: 37px; top: 55px; width: 557px; height: 418px; }
  .slide--bullets { left: 622px; top: 55px; width: 558px; height: 420px; }
  .slide--chart { left: 37px; top: 540px; width: 559px; height: 420px; }

  .brand {
    position: absolute;
    display: flex; align-items: center; gap: 7px;
    color: var(--dark-blue);
    font-weight: 700;
    font-size: 21px;
    letter-spacing: -0.2px;
  }
  .brand__dot { width: 20px; height: 20px; border-radius: 50%; background: var(--orange); }

  /* title slide */
  .hero {
    position: absolute; left: 0; top: 0; width: 100%; height: 291px;
    background: linear-gradient(90deg, var(--band-start) 0%, #0a4f95 45%, var(--band-end) 100%);
  }
  .hero__strip { position: absolute; left: 0; top: 291px; width: 100%; height: 8px; background: var(--strip-blue); }
  .hero__bar { position: absolute; left: 0; top: 299px; width: 100%; height: 11px; background: var(--orange); }
  .slide--title .brand { right: 20px; top: 324px; font-size: 24px; }
  .slide--title .brand__dot { width: 23px; height: 23px; }
  .deck-title { position: absolute; left: 20px; top: 321px; font-size: 24px; color: var(--orange); font-weight: 400; }
  .deck-subtitle { position: absolute; left: 20px; top: 372px; font-size: 16px; color: var(--grey); }

  /* content slides */
  .header {
    position: absolute; left: 0; top: 0; width: 100%; height: 71px;
    background: linear-gradient(90deg, var(--band-start) 0%, #0a4f95 50%, var(--band-end) 100%);
  }
  .header__title {
    position: absolute; left: 19px; top: 24px;
    color: #fff; font-size: 20px; font-weight: 400; white-space: nowrap;
  }
  .slide .brand--small { right: 12px; top: 77px; }
  .footer-bar { position: absolute; left: 0; bottom: 0; width: 100%; height: 9px; background: var(--orange); }

  .bullets { position: absolute; left: 20px; top: 116px; width: 505px; list-style: none; font-size: 15.5px; line-height: 18px; }
  .bullets > li { position: relative; padding-left: 20px; margin-bottom: 9px; }
  .bullets > li::before {
    content: ""; position: absolute; left: 2px; top: 4px;
    width: 9px; height: 9px; border-radius: 50%; background: var(--orange);
  }
  .bullets ul { list-style: none; margin-top: 13px; font-size: 13.5px; line-height: 17px; }
  .bullets ul li { position: relative; padding-left: 24px; margin-bottom: 10px; }
  .bullets ul li::before { content: "–"; position: absolute; left: 2px; top: 0; color: var(--orange); }

  /* chart slide */
  .map-ghost {
    position: absolute; left: 30px; top: 110px; width: 500px; height: 260px;
    background: radial-gradient(ellipse at center, rgba(237,110,0,0.06) 0%, rgba(237,110,0,0.03) 55%, rgba(255,255,255,0) 75%);
  }
  .chart-title { position: absolute; left: 0; width: 528px; top: 110px; text-align: center; font-family: "Carlito", Calibri, sans-serif; font-weight: 700; font-size: 15px; }
  .donut { position: absolute; left: 148px; top: 146px; }
  .legend { position: absolute; left: 395px; top: 195px; list-style: none; font-family: "Carlito", Calibri, sans-serif; font-size: 13px; }
  .legend li { display: flex; align-items: center; gap: 6px; height: 21.5px; }
  .legend__swatch { width: 8px; height: 8px; }
  .q1 { background: var(--orange); }
  .q2 { background: var(--light-blue); }
  .q3 { background: var(--dark-blue); }
  .q4 { background: var(--orange-deep); }
</style>
</head>
<body>

<section class="slide slide--title">
  <div class="hero" role="img" aria-label="World map with location markers over a blue gradient"></div>
  <div class="hero__strip"></div>
  <div class="hero__bar"></div>
  <h1 class="deck-title">Lorem ipsum dolor sit amet</h1>
  <p class="deck-subtitle">Nam non mi velit</p>
  <div class="brand"><span class="brand__dot"></span>Corvanta</div>
</section>

<section class="slide slide--bullets">
  <div class="header">
    <h2 class="header__title">Lorem ipsum dolor sit amet, consectetur adipiscing</h2>
  </div>
  <div class="brand brand--small"><span class="brand__dot"></span>Corvanta</div>
  <ul class="bullets">
    <li>Lorem ipsum dolor sit amet, consectetur adipiscing elit. Phasellus vitae egestas elit.</li>
    <li>Quisque faucibus volutpat magna, at varius ligula lacinia eget. Maecenas hendrerit mi eu lorem pretium eu porttitor libero tempor. Ut pretium purus non enim semper imperdiet.
      <ul>
        <li>Nunc tincidunt fringilla nulla, vel lobortis risus vulputate commodo.</li>
        <li>Mauris ut lacus neque. Sed vitae nunc non enim placerat iaculis id ut mauris.</li>
      </ul>
    </li>
    <li>Nam non mi velit. Lorem ipsum dolor sit amet, consectetur adipiscing elit. In sed nisi est. Vestibulum volutpat leo vitae diam tincidunt vulputate. Suspendisse vitae nisi elit, non aliquam mi. Nulla suscipit pharetra varius. Ut pretium purus non enim semper imperdiet.</li>
  </ul>
  <div class="footer-bar"></div>
</section>

<section class="slide slide--chart">
  <div class="header">
    <h2 class="header__title">Lorem ipsum dolor sit amet, consectetur adipiscing</h2>
  </div>
  <div class="brand brand--small"><span class="brand__dot"></span>Corvanta</div>
  <div class="map-ghost" role="img" aria-label="Faint world map watermark behind the chart"></div>
  <h3 class="chart-title">Graphic Title</h3>
  <svg class="donut" width="180" height="180" viewBox="-90 -90 180 180" font-family="Carlito, Calibri, sans-serif" font-size="12.5" fill="#fff" text-anchor="middle">
    <path d="M0,-89 A89,89 0 1 1 -47.7,75.1 L-24.1,38 A45,45 0 1 0 0,-45 Z" fill="#ed6e00"/>
    <path d="M-47.7,75.1 A89,89 0 0 1 -88.8,-5.6 L-44.9,-2.8 A45,45 0 0 0 -24.1,38 Z" fill="#006ec7"/>
    <path d="M-88.8,-5.6 A89,89 0 0 1 -60.9,-64.9 L-30.8,-32.8 A45,45 0 0 0 -44.9,-2.8 Z" fill="#0f1f7a"/>
    <path d="M-60.9,-64.9 A89,89 0 0 1 0,-89 L0,-45 A45,45 0 0 0 -30.8,-32.8 Z" fill="#c0480a"/>
    <text x="63" y="24">59%</text>
    <text x="-59" y="35">17%</text>
    <text x="-59" y="-24">12%</text>
    <text x="-24" y="-56">12%</text>
  </svg>
  <ul class="legend">
    <li><span class="legend__swatch q1"></span>1st Qtr</li>
    <li><span class="legend__swatch q2"></span>2nd Qtr</li>
    <li><span class="legend__swatch q3"></span>3rd Qtr</li>
    <li><span class="legend__swatch q4"></span>4th Qtr</li>
  </ul>
  <div class="footer-bar"></div>
</section>

</body>
</html>
```